Coffee House With Cycling Theme Wants Business Cards

We want to create a business card for a coffee house that has a cycling theme. We expect to use the current logo on one side of the business card and we have been considering adding the words 'COFFEE HOUSE' underneath (see example). For the other side of the business card we want an interesting design with tag-line, address and social media links (the normal business card stuff). See examples provided but we are not fixed on having it exactly as shown, we are very open to great creative ideas. Please note our logo has the initials ‘RM' in orange embedded in the design and this must be retained. However, you can play with the words COFFEE HOUSE as well as use the orange color on the backside of the business card, as you see fit. For an image on the backside of the business card it can be a photo, hand-drawn or whatever but it must visually combine coffee and cycling in some way. The interior of the Coffee House will be reclaimed wood, rustic and have an urban feel to it with cycling artifacts hanging from the walls/ceiling, etc. Finally, it would be beneficial if the business card design elements can be easily used on flyers and other promotional assets. Good luck, we are looking forward to seeing your creative ideas.

Target Market(s)

Coffee lovers and cycling fans

Contact Information for Business Card

See project description.

Colors

Designer to choose colors to be used in the design.

Requirements
Must have
• Must use the current logo provided and combine a coffee and bike theme.
Nice to have
• Orange is used in current logo and could be used as an accent color on the backside of the business card.

```html
<!DOCTYPE html>
<html lang="en">
<head>
<meta charset="utf-8">
<title>RM Coffee House – Business Cards</title>
<link href="https://fonts.googleapis.com/css2?family=Roboto+Condensed:wght@400;700&display=swap" rel="stylesheet">
<style>
  :root {
    --backdrop: #5d7c80;
    --card-white: #fbfbfb;
    --charcoal: #3d3c3c;
    --pattern-light: #8d8c8c;
    --pattern-mid: #5e5d5d;
    --orange: #f26a24;
    --orange-dark: #c94f16;
    --text-light: #ffffff;
    --faint-orange: #f8cdb4;
  }
  * { margin: 0; padding: 0; box-sizing: border-box; }
  html, body { width: 1200px; height: 805px; overflow: hidden; }
  body {
    background: var(--backdrop);
    font-family: "Roboto Condensed", "Arial Narrow", sans-serif;
    position: relative;
  }
  .card {
    position: absolute;
    left: 326px;
    width: 542px;
    border-radius: 28px;
    overflow: hidden;
    background: var(--card-white);
  }
  .card--front { top: 77px; height: 312px; }
  .card--back { top: 436px; height: 303px; }

  /* Front */
  .front-logo {
    position: absolute;
    left: 0; right: 0; top: 44px;
    text-align: center;
  }
  .front-logo__initials {
    display: block;
    font-weight: 700;
    font-size: 96px;
    line-height: 96px;
    color: var(--orange);
    letter-spacing: 2px;
  }
  .front-logo__words {
    display: block;
    margin-top: 8px;
    font-weight: 700;
    font-size: 46px;
    line-height: 46px;
    color: var(--charcoal);
  }
  .accent-band {
    position: absolute;
    left: 0; width: 100%;
    height: 24px;
  }
  .card--front .accent-band { top: 209px; }
  .card--back .accent-band { top: 162px; }
  .cup-pattern {
    position: absolute;
    left: 0; top: 233px;
    width: 100%; height: 79px;
    background:
      linear-gradient(180deg, var(--pattern-light) 0%, var(--pattern-mid) 45%, var(--pattern-light) 55%, var(--pattern-mid) 100%);
  }

  /* Back */
  .back-mark {
    position: absolute;
    left: 0; top: 0;
    width: 285px; height: 162px;
    display: flex; align-items: center; justify-content: center;
  }
  .back-mark__initials {
    font-weight: 700;
    font-size: 110px;
    color: var(--faint-orange);
    letter-spacing: 2px;
  }
  .latte-photo {
    position: absolute;
    left: 285px; top: 0;
    width: 257px; height: 162px;
    background: radial-gradient(circle at 40% 60%, #c79a6c 0%, #9b6a3f 35%, #5a3a22 60%, #2e231d 85%);
  }
  .back-info {
    position: absolute;
    left: 0; top: 186px;
    width: 100%; height: 117px;
    background: var(--charcoal);
    color: var(--text-light);
    text-align: center;
  }
  .tagline {
    margin-top: 14px;
    font-weight: 700;
    font-size: 19px;
    line-height: 22px;
    display: flex; align-items: center; justify-content: center; gap: 8px;
  }
  .address {
    margin-top: 4px;
    font-size: 16px;
    line-height: 18px;
  }
  .social-row {
    margin-top: 8px;
    display: flex; justify-content: center; align-items: center; gap: 14px;
    font-size: 20px;
  }
  .social-item { display: flex; align-items: center; gap: 7px; }
  .social-square {
    width: 20px; height: 20px;
    background: var(--orange);
    display: flex; align-items: center; justify-content: center;
  }
</style>
</head>
<body>

<section class="card card--front" aria-label="Business card front">
  <div class="front-logo">
    <span class="front-logo__initials">RM</span>
    <span class="front-logo__words">COFFEE HOUSE</span>
  </div>
  <svg class="accent-band" viewBox="0 0 542 24" preserveAspectRatio="none" aria-hidden="true">
    <rect x="0" y="0" width="542" height="24" fill="#f26a24"/>
    <polygon points="258,0 271,3 284,0 284,24 271,21 258,24" fill="#c94f16"/>
  </svg>
  <div class="cup-pattern" role="img" aria-label="Repeating pattern of white coffee cups on charcoal"></div>
</section>

<section class="card card--back" aria-label="Business card back">
  <div class="back-mark">
    <span class="back-mark__initials">RM</span>
  </div>
  <div class="latte-photo" role="img" aria-label="Photo of a latte with a bicycle drawn in the foam"></div>
  <svg class="accent-band" viewBox="0 0 542 24" preserveAspectRatio="none" aria-hidden="true">
    <rect x="0" y="0" width="542" height="24" fill="#f26a24"/>
    <polygon points="258,0 271,3 284,0 284,24 271,21 258,24" fill="#c94f16"/>
  </svg>
  <div class="back-info">
    <p class="tagline">YOUR TAG LINE YOUR TAG LINE
      <svg width="22" height="22" viewBox="0 0 22 22" aria-hidden="true">
        <path d="M3 10 h13 v4 a5 5 0 0 1 -5 5 h-3 a5 5 0 0 1 -5 -5 z" fill="#f26a24"/>
        <path d="M16 11 h2 a2.5 2.5 0 0 1 0 5 h-2" fill="none" stroke="#f26a24" stroke-width="1.6"/>
        <rect x="2" y="20" width="16" height="1.6" fill="#f26a24"/>
        <path d="M8 3 q2 2 0 4 M11 2 q2 2 0 5" fill="none" stroke="#f26a24" stroke-width="1.3"/>
      </svg>
    </p>
    <p class="address">Your Street Address<br>Your Street Address</p>
    <div class="social-row">
      <span class="social-item">
        <span class="social-square">
          <svg width="14" height="14" viewBox="0 0 14 14" aria-hidden="true">
            <circle cx="7" cy="7" r="5.5" fill="none" stroke="#fff" stroke-width="1.2"/>
            <ellipse cx="7" cy="7" rx="2.4" ry="5.5" fill="none" stroke="#fff" stroke-width="1"/>
            <path d="M1.5 7 h11" stroke="#fff" stroke-width="1"/>
          </svg>
        </span>rmcoffeehouse.com</span>
      <span class="social-item"><span class="social-square"></span>rmcoffeehouse</span>
      <span class="social-item"><span class="social-square"></span>rmcoffeehouse</span>
    </div>
  </div>
</section>

</body>
</html>
```